Copper Mesa Rides, need businesscard design and cool logo

we are a new business in dubai that sells and buys ATV, Dirtbikes, jetski and buggys for the arab region. we have the latest models in mint condition. we are looking for someone to come up with a super cool business card design and logo for our new company.

We really like how ''Quelta'', ''Brimvolt'' & ''Pell racing'' have their design layout and we are looking for something along those lines. We are also open for other suggestions if it looks super cool.

One side should be normal company info such as:
Nameof representative: Marcus Ellendorf
mobile: 0097 155 382 4416
whatsapp: 0097 155 382 4416
instigram: coppermesarides
email: mellendorf@quillpost.net

The other side should be a cool design of some sort that incorporates or stands for our name ''Copper Mesa Rides''. it could also be something creative regarding offroading.

Target Market(s)

offroad segment

Industry/Entity Type

Business

Contact Information for Business Card

details are mentioned in the description above.

Requirements
Must have
• very attractive business card with a cool layout
• we have included some pictures, but this is just something that looks cool, we are open to something along those lines.
Nice to have
• We really like how ''Quelta'', ''Brimvolt'' & ''Pell racing'' have their design layout and we are looking for something along those lines. We are also open for other suggestions if it looks super cool.
Should not have
• it should not be plain, boring, dull and cheep that could be found online.

```html
<!DOCTYPE html>
<html lang="en">
<head>
<meta charset="utf-8">
<title>Copper Mesa Rides – Business Card</title>
<link rel="stylesheet" href="https://fonts.googleapis.com/css2?family=Noto+Sans:wght@700;800&family=Kalam:wght@400&display=swap">
<style>
  :root {
    --page: #ffffff;
    --card: #000000;
    --gold: #c2a63f;
    --ink: #ffffff;
    --phone-red: #c7332b;
    --chat-green: #2fa84f;
  }
  * { box-sizing: border-box; margin: 0; padding: 0; }
  html, body {
    width: 1200px; height: 1200px; overflow: hidden;
    background: var(--page);
    font-family: "Noto Sans", Arial, sans-serif;
  }
  .card {
    position: absolute; left: 299px; width: 571px; height: 326px;
    background: var(--card); overflow: hidden; color: var(--ink);
  }
  .card--front { top: 224px; }
  .card--back { top: 774px; }

  .brand {
    position: absolute; left: 0; width: 100%;
    text-align: center; color: var(--gold);
    font-weight: 800; line-height: 1; letter-spacing: 2px;
  }
  .card--front .brand { top: 36px; font-size: 50px; }
  .card--back .brand { top: 92px; font-size: 47px; }
  .brand__line { display: block; margin-bottom: 8px; }

  .connectors { position: absolute; inset: 0; }
  .connectors line { stroke: var(--gold); stroke-linecap: round; }

  .info { position: absolute; font-weight: 700; white-space: nowrap; line-height: 1; }
  .rep-name { left: 0; width: 557px; text-align: center; top: 175px; font-size: 21px; }
  .social { left: 10px; top: 237px; font-size: 18px; display: flex; align-items: center; gap: 6px; }
  .social__mark { width: 18px; height: 18px; border-radius: 4px; background: var(--gold); }
  .email { right: 317px; top: 275px; font-size: 18px; }
  .phone { left: 341px; top: 275px; font-size: 19px; letter-spacing: 0.3px; }
  .contact-icons { position: absolute; left: 413px; top: 241px; display: flex; gap: 12px; align-items: center; }
  .chat-mark { width: 19px; height: 19px; border-radius: 50%; background: var(--chat-green); }

  .tagline {
    position: absolute; left: 0; width: 100%; top: 240px;
    text-align: center; font-family: "Kalam", cursive;
    font-size: 31px; color: var(--ink);
  }
</style>
</head>
<body>
  <section class="card card--front" aria-label="Business card front">
    <h1 class="brand"><span class="brand__line">COPPER MESA</span><span class="brand__line">RIDES</span></h1>

    <svg class="connectors" width="571" height="326" aria-hidden="true">
      <line x1="205" y1="201" x2="355" y2="201" stroke-width="7"/>
      <line x1="299" y1="201" x2="299" y2="330" stroke-width="8"/>
      <line x1="184" y1="246" x2="297" y2="245" stroke-width="6"/>
      <line x1="262" y1="283" x2="337" y2="283" stroke-width="6"/>
    </svg>

    <p class="info rep-name">Marcus Ellendorf</p>
    <p class="info social"><span class="social__mark" aria-hidden="true"></span>coppermesarides</p>
    <p class="info email">mellendorf@quillpost.net</p>

    <div class="contact-icons" aria-hidden="true">
      <svg width="14" height="20" viewBox="0 0 14 20">
        <rect x="1" y="2" width="12" height="17" rx="2" fill="var(--phone-red)"/>
        <rect x="3" y="4" width="8" height="5" fill="#fff"/>
        <rect x="9" y="0" width="2" height="3" fill="var(--phone-red)"/>
        <g fill="#fff"><rect x="3" y="11" width="2" height="2"/><rect x="6" y="11" width="2" height="2"/><rect x="9" y="11" width="2" height="2"/><rect x="3" y="14" width="2" height="2"/><rect x="6" y="14" width="2" height="2"/><rect x="9" y="14" width="2" height="2"/></g>
      </svg>
      <span class="chat-mark"></span>
    </div>
    <p class="info phone">0097 155 382 4416</p>
  </section>

  <section class="card card--back" aria-label="Business card back">
    <h2 class="brand"><span class="brand__line">COPPER MESA</span><span class="brand__line">RIDES</span></h2>
    <p class="tagline">Your fun begins with us</p>
  </section>
</body>
</html>
```